Design a building access mobile app for Tally by Halvorn Portal Systems

Hello, We're looking for an awesome designer to create an app design for our app Tally, by Halvorn Portal Systems. the mobile app allows employees open their office doors with their mobile phone. this means they don't have to use those plastic card badges or keys. We like clean modern design, dark and light themes. We don't have a logo yet.
Updates

Reason: Waiting on a couple designers to submit concepts

Target Market(s)

Commercial and employees

Industry/Entity Type

Building

Font styles to use
Sans Serif
Other font styles liked:
• Oswald extra light

Requirements
Must have
• nice clean design

```html
<!DOCTYPE html>
<html lang="en">
<head>
<meta charset="utf-8">
<title>Halvorn Security – Door Access</title>
<link rel="stylesheet" href="https://fonts.googleapis.com/css2?family=Oswald:wght@300;400&family=Roboto:wght@400&display=swap">
<style>
  :root {
    --teal: #2fc6d3;
    --blue: #2a78c2;
    --blue-mid: #3a98d8;
    --white: #ffffff;
    --line: #e6eaee;
    --arrow: #4a9fe0;
  }
  * { margin: 0; padding: 0; box-sizing: border-box; }
  html, body { width: 675px; height: 1200px; overflow: hidden; background: var(--white); }
  .app { position: relative; width: 675px; height: 1200px; overflow: hidden; font-family: "Oswald", sans-serif; }

  .hero {
    position: absolute; left: 0; top: 0; width: 675px; height: 563px;
    background: linear-gradient(160deg, var(--teal) 0%, #2ea8cc 45%, var(--blue) 100%);
    color: var(--white);
  }
  .status-bar {
    position: absolute; top: 0; left: 0; right: 0; height: 45px;
    display: flex; align-items: center; justify-content: space-between;
    padding: 0 14px; font-family: "Roboto", sans-serif; font-size: 24px;
  }
  .status-left, .status-right { display: flex; align-items: center; gap: 8px; }
  .status-time { position: absolute; left: 0; right: 0; text-align: center; font-weight: 400; }

  .nav-bar {
    position: absolute; top: 45px; left: 0; right: 0; height: 60px;
    display: flex; align-items: center; justify-content: center;
  }
  .menu-icon { position: absolute; left: 24px; top: 16px; }
  .nav-title { font-weight: 300; font-size: 27px; letter-spacing: 1px; text-transform: uppercase; }

  .location-pin {
    position: absolute; left: 297px; top: 196px; width: 81px; height: 81px;
    border-radius: 50%; background: var(--white);
    display: flex; align-items: center; justify-content: center;
  }
  .address {
    position: absolute; top: 318px; left: 0; right: 0; text-align: center;
    font-weight: 300; font-size: 45px; line-height: 74px;
  }

  .door-selector { position: absolute; top: 563px; left: 0; width: 675px; height: 637px; }
  .divider { position: absolute; left: 337px; top: 60px; width: 1px; height: 560px;
    background: linear-gradient(to bottom, transparent, var(--line) 20%, var(--line) 80%, transparent); }
  .door-button {
    position: absolute; left: 197px; top: 186px; width: 280px; height: 280px;
    border-radius: 50%; border: 4px solid var(--blue-mid); background: var(--white);
    display: flex; align-items: center; justify-content: center;
  }
  .door-button-inner {
    width: 250px; height: 250px; border-radius: 50%;
    background: radial-gradient(circle at 40% 35%, #5fb6ea, var(--blue-mid) 75%);
    color: var(--white); display: flex; flex-direction: column; align-items: center; justify-content: center;
    font-weight: 400; font-size: 28px; line-height: 38px; letter-spacing: 1px; text-align: center;
  }
  .nav-arrow { position: absolute; top: 302px; }
  .nav-arrow.prev { left: 64px; }
  .nav-arrow.next { left: 580px; }
</style>
</head>
<body>
<div class="app">
  <header class="hero">
    <div class="status-bar">
      <div class="status-left">
        <svg width="62" height="14" viewBox="0 0 62 14"><g fill="#fff"><circle cx="6" cy="7" r="5"/><circle cx="18" cy="7" r="5"/><circle cx="30" cy="7" r="5"/></g><g fill="none" stroke="#fff" stroke-width="1.5"><circle cx="42" cy="7" r="4.3"/><circle cx="54" cy="7" r="4.3"/></g></svg>
        <span>Nimbo</span>
        <svg width="24" height="18" viewBox="0 0 24 18"><path d="M12 17 L1 5 A16 16 0 0 1 23 5 Z" fill="#fff"/></svg>
      </div>
      <div class="status-time">1:23 AM</div>
      <div class="status-right">
        <svg width="12" height="20" viewBox="0 0 12 20"><path d="M1 5 L11 14 L6 19 V1 L11 6 L1 15" fill="none" stroke="#fff" stroke-width="1.6"/></svg>
        <span>77%</span>
        <svg width="46" height="20" viewBox="0 0 46 20"><rect x="1" y="1" width="40" height="18" rx="4" fill="none" stroke="#fff" stroke-width="1.6"/><rect x="4" y="4" width="28" height="12" rx="2" fill="#fff"/><rect x="42" y="7" width="3" height="6" rx="1" fill="#fff"/></svg>
      </div>
    </div>
    <nav class="nav-bar">
      <svg class="menu-icon" width="40" height="28" viewBox="0 0 40 28"><g stroke="#fff" stroke-width="3"><line x1="0" y1="2" x2="40" y2="2"/><line x1="0" y1="14" x2="40" y2="14"/><line x1="0" y1="26" x2="40" y2="26"/></g></svg>
      <h1 class="nav-title">Halvorn Security</h1>
    </nav>
    <div class="location-pin">
      <svg width="30" height="44" viewBox="0 0 30 44"><path d="M15 0 C6.7 0 0 6.7 0 15 C0 26 15 44 15 44 C15 44 30 26 30 15 C30 6.7 23.3 0 15 0 Z" fill="#3a8fd6"/><circle cx="15" cy="15" r="5.5" fill="#fff"/></svg>
    </div>
    <p class="address">2280 NE Larkspur Parkway<br>Seattle, WA 98107</p>
  </header>

  <main class="door-selector">
    <div class="divider"></div>
    <svg class="nav-arrow prev" width="30" height="54" viewBox="0 0 30 54"><polyline points="26,2 4,27 26,52" fill="none" stroke="#4a9fe0" stroke-width="3.5"/></svg>
    <button class="door-button" type="button" aria-label="Unlock Front Door">
      <span class="door-button-inner"><span>FRONT DOOR</span><span>(F-3D4G)</span></span>
    </button>
    <svg class="nav-arrow next" width="30" height="54" viewBox="0 0 30 54"><polyline points="4,2 26,27 4,52" fill="none" stroke="#4a9fe0" stroke-width="3.5"/></svg>
  </main>
</div>
</body>
</html>
```